Online business manager needs a website

I need a website designed and then coded. I am an online business manager serving a number of different industries providing administrative support to existing small businesses and helping solo practitioners get their new business up and running.

I didn't have a logo formally designed but have been using the attached avatar and wouldn't mind something that incorporated that.

The business doesn't have an official name, so I've just been using my name Lena Pruvost, Online Business Manager or Lena Pruvost, OBM. I've attached two documents that I have made previously for an example of content.

I would prefer the final site be in Wordpress.

Requirements
Must have
• A way to contact me, testimonials, list of services

```html
<!DOCTYPE html>
<html lang="en">
<head>
<meta charset="utf-8">
<title>Lena Pruvost – Online Business Manager</title>
<link href="https://fonts.googleapis.com/css2?family=Poppins:wght@400;500;600;700&family=Inter:wght@400;500;600&display=swap" rel="stylesheet">
<style>
:root{
  --mint:#bfe8e1;
  --mint-soft:#d6f1ec;
  --mint-pale:#e4f6f2;
  --teal:#3b9db1;
  --teal-deep:#2f8396;
  --ink:#1d2a2e;
  --text:#2a3235;
  --muted:#5c6669;
  --purple:#9c7fc9;
  --paper:#f6f7f7;
  --white:#ffffff;
  --field:#e5e6e7;
}
*{box-sizing:border-box;margin:0;padding:0}
html,body{width:1200px;height:4076px;overflow:hidden}
body{position:relative;background:var(--paper);font-family:"Inter",sans-serif;color:var(--text)}
.abs{position:absolute}
h1,h2,h3,.heading{font-family:"Poppins",sans-serif;color:var(--ink)}
.eyebrow{font-family:"Inter",sans-serif;font-size:12px;letter-spacing:.5px;text-transform:uppercase;color:var(--teal)}
.btn{position:absolute;display:flex;align-items:center;justify-content:center;gap:7px;background:var(--teal);color:var(--white);font-size:11px;font-weight:500;border-radius:3px;box-shadow:3px 3px 0 var(--ink)}
.btn .tick{width:12px;height:12px;border-radius:50%;background:var(--white);display:flex;align-items:center;justify-content:center}
.placeholder{position:absolute}
/* header */
.nav{position:absolute;top:35px;left:415px;display:flex;gap:16px;font-size:12px;color:var(--ink)}
.nav .active{font-weight:600}
/* hero */
.hero-title{position:absolute;left:195px;top:138px;font-size:38px;line-height:45px;font-weight:600}
.hero-copy{position:absolute;left:195px;top:290px;width:370px;font-size:11.5px;line-height:19px;color:var(--text)}
.stat-card{position:absolute;background:var(--white);border-radius:8px;box-shadow:4px 4px 0 var(--ink)}
/* about */
.about-title{position:absolute;left:640px;top:726px;font-size:31px;font-weight:600}
.about-sub{position:absolute;left:640px;top:766px;font-size:19px;font-weight:600;color:var(--ink);font-family:"Poppins",sans-serif}
.about-copy{position:absolute;left:640px;top:808px;width:372px;font-size:11px;line-height:19.8px}
/* services */
.service-card{position:absolute;top:1460px;width:185px;height:202px;background:var(--white);box-shadow:0 2px 6px rgba(0,0,0,.06);padding:28px 20px}
.service-card h3{font-size:18px;line-height:22px;font-weight:600;margin-top:22px}
.service-card .link{position:absolute;left:20px;bottom:28px;font-size:11px;color:var(--teal)}
.service-card.active{background:var(--teal);box-shadow:5px 5px 0 var(--ink)}
.service-card.active h3,.service-card.active .link{color:var(--white)}
.service-card.faded{opacity:.3}
.arrow-btn{position:absolute;width:46px;height:46px;border-radius:50%;display:flex;align-items:center;justify-content:center}
/* pricing */
.plan{position:absolute;font-size:10px}
.plan .price{font-family:"Poppins",sans-serif;font-size:22px;font-weight:500;color:var(--ink)}
.plan .price small{font-size:10px;font-weight:400;margin-left:6px}
.plan .name{font-family:"Poppins",sans-serif;font-size:17px;font-weight:500;color:var(--ink);margin-top:12px}
.plan .desc{font-size:9.5px;line-height:12px;margin-top:6px;color:var(--text);width:160px}
.plan ul{list-style:none;margin-top:12px}
.plan li{display:flex;align-items:center;gap:8px;height:21.5px;font-size:9.5px}
.plan li i{width:11px;height:11px;border-radius:50%;background:#a6cfd6;display:inline-block}
.plan li.off{color:#9aa3a5}
.plan.popular .price,.plan.popular .name,.plan.popular .desc,.plan.popular li{color:var(--white)}
.plan.popular li i{background:rgba(255,255,255,.45)}
/* testimonial */
.quote-text{position:absolute;left:215px;width:770px;text-align:center;top:2700px;font-family:"Poppins",sans-serif;font-size:20.5px;line-height:31px;color:var(--ink);font-weight:500}
/* contact */
.contact-item{position:absolute;left:258px;display:flex;align-items:center;gap:16px;font-family:"Poppins",sans-serif;font-size:21px;color:var(--white);line-height:25px}
.contact-item .ico{width:58px;height:58px;border-radius:50%;background:var(--ink);display:flex;align-items:center;justify-content:center;flex-shrink:0}
.field{position:absolute;background:var(--field);font-size:9.5px;color:var(--ink);padding:9px 8px}
/* footer */
.foot-col{position:absolute;top:3780px;font-size:10.5px;color:var(--white);line-height:24.5px}
.foot-col h4{font-size:11.5px;font-weight:600;margin-bottom:6px}
</style>
</head>
<body>

<!-- HERO -->
<svg class="abs" style="left:0;top:0" width="1200" height="620" viewBox="0 0 1200 620">
  <path d="M0 0H1200V560L600 505L0 580Z" fill="var(--mint)"/>
  <path d="M0 592L600 515L1200 572V612L600 532L0 616Z" fill="var(--teal)"/>
</svg>

<div class="placeholder" role="img" aria-label="Cartoon avatar of Lena at a laptop" style="left:197px;top:19px;width:82px;height:63px;background:linear-gradient(#e9d39b,#8fa3a8);border-radius:6px"></div>
<nav class="nav"><span class="active">Home</span><span>About Us</span><span>Services</span><span>Pricing</span><span>Testimonials</span><span>Contact Us</span></nav>
<div class="btn" style="left:910px;top:27px;width:105px;height:30px;font-size:9.5px">
  <svg width="11" height="11" viewBox="0 0 24 24"><path d="M6.6 10.8a15 15 0 006.6 6.6l2.2-2.2c.3-.3.7-.4 1-.2 1.1.4 2.3.6 3.6.6.6 0 1 .4 1 1V20c0 .6-.4 1-1 1A17 17 0 013 4c0-.6.4-1 1-1h3.5c.6 0 1 .4 1 1 0 1.3.2 2.5.6 3.6.1.3 0 .7-.2 1z" fill="var(--ink)"/></svg>
  555.014.2288</div>

<h1 class="hero-title">Hello, I’m<br>Lena Pruvost An Online<br>Business Manager</h1>
<p class="hero-copy">Serving a number of different industries providing administrative support to existing small businesses and helping solo practitioners get their new business up and running.</p>
<div class="btn" style="left:195px;top:370px;width:111px;height:32px"><span class="tick"><svg width="8" height="8" viewBox="0 0 10 10"><path d="M2 5l2 2 4-4" stroke="var(--teal)" stroke-width="1.6" fill="none"/></svg></span>Contact Now</div>

<svg class="abs" style="left:660px;top:180px" width="410" height="370" viewBox="0 0 410 370"><path d="M60 40Q200-10 330 40L380 120Q410 260 330 350H70Q0 260 20 130Z" fill="var(--teal)"/></svg>
<div class="placeholder" role="img" aria-label="Photo of Lena smiling, holding a laptop and waving" style="left:760px;top:78px;width:270px;height:462px;background:linear-gradient(180deg,#6e5a4e 0%,#d9d6d0 40%,#e8e8e6 100%);border-radius:120px 120px 0 0"></div>

<div class="stat-card" style="left:625px;top:222px;width:166px;height:79px">
  <div class="abs" style="left:14px;top:18px;width:44px;height:44px;border-radius:50%;background:var(--mint-soft);display:flex;align-items:center;justify-content:center">
    <svg width="22" height="22" viewBox="0 0 24 24"><path d="M12 2l3 6.5 7 .8-5.2 4.8 1.4 7L12 17.6 5.8 21l1.4-7L2 9.3l7-.8z" fill="var(--teal)"/></svg></div>
  <div class="abs" style="left:74px;top:18px;font-size:8px;color:var(--muted)">RATING</div>
  <div class="abs" style="left:74px;top:28px;font-family:Poppins,sans-serif;font-size:21px;font-weight:600;color:var(--ink)">4.0</div>
  <div class="abs" style="left:74px;top:56px;font-size:7px;color:#2aa653">+18% <span style="color:var(--muted)">since last week</span></div>
</div>
<div class="stat-card" style="left:934px;top:416px;width:142px;height:79px">
  <div class="abs" style="left:10px;top:8px;font-size:8px;color:var(--ink)">Insights</div>
  <div class="abs" style="right:8px;top:7px;font-size:8px;color:#e8902a">● On track</div>
  <svg class="abs" style="left:12px;top:30px" width="118" height="40" viewBox="0 0 118 40">
    <g fill="var(--purple)"><rect x="2" y="14" width="5" height="26" rx="2"/><rect x="16" y="22" width="5" height="18" rx="2"/><rect x="30" y="8" width="5" height="32" rx="2"/><rect x="44" y="18" width="5" height="22" rx="2"/><rect x="58" y="4" width="5" height="36" rx="2"/><rect x="72" y="20" width="5" height="20" rx="2"/><rect x="86" y="10" width="5" height="30" rx="2"/><rect x="100" y="16" width="5" height="24" rx="2"/></g></svg>
</div>

<!-- ABOUT -->
<div class="abs" style="left:218px;top:665px;width:317px;height:435px;border-radius:26px;background:var(--ink)"></div>
<div class="placeholder" role="img" aria-label="Photo of Lena working on a laptop by a window" style="left:226px;top:665px;width:309px;height:427px;border-radius:26px;background:linear-gradient(160deg,#6fb3b0 0%,#c98a4e 55%,#f0a45a 100%)"></div>
<div class="abs" style="left:232px;top:995px;width:220px;height:90px;border-radius:14px;background:#f4b86a"></div>
<div class="abs" style="left:246px;top:1008px;width:66px;height:66px;border-radius:50%;background:var(--white);display:flex;align-items:center;justify-content:center"><svg width="22" height="22" viewBox="0 0 24 24"><path d="M7 4l14 8-14 8z" fill="var(--teal)"/></svg></div>
<div class="abs" style="left:326px;top:1032px;font-family:Poppins,sans-serif;font-size:14px;font-weight:500;color:var(--ink)">Watch My Story</div>
<div class="abs" style="left:174px;top:712px;width:118px;height:74px;background:var(--white);border-radius:12px 12px 12px 0;box-shadow:4px 4px 0 var(--ink);padding:11px 20px;font-family:Poppins,sans-serif;font-size:14px;line-height:17px;color:var(--ink)">Virtual<br>Assistant<div style="font-size:10px;margin-top:4px">— Lena Pruvost</div></div>
<div class="abs" style="left:438px;top:950px;width:158px;height:161px;background:var(--purple);border-radius:16px;box-shadow:0 0 0 3px var(--ink)">
  <div class="abs" role="img" aria-label="Small portrait of Lena" style="left:12px;top:12px;width:28px;height:28px;border-radius:50%;background:#8a5e45"></div>
  <div class="abs" style="left:48px;top:14px;font-family:Poppins,sans-serif;font-size:13px;color:var(--white)">Lena Pruvost</div>
  <div class="abs" style="left:48px;top:32px;font-size:7px;color:#e8e0f4">Contact Details</div>
  <div class="abs" style="left:12px;top:55px;width:136px;height:40px;background:var(--ink);border-radius:7px"></div>
  <div class="abs" style="left:18px;top:62px;width:26px;height:26px;border-radius:5px;background:var(--teal);display:flex;align-items:center;justify-content:center"><svg width="14" height="10" viewBox="0 0 14 10"><rect x=".5" y=".5" width="13" height="9" fill="none" stroke="#fff"/><path d="M.5.5l6.5 5 6.5-5" stroke="#fff" fill="none"/></svg></div>
  <div class="abs" style="left:52px;top:64px;font-size:6.5px;line-height:10px;color:var(--white)">Email address<br><b>@LenaPruvost7</b></div>
  <div class="abs" style="left:12px;top:104px;width:136px;height:40px;background:var(--ink);border-radius:7px"></div>
  <div class="abs" style="left:18px;top:111px;width:26px;height:26px;border-radius:50%;background:var(--mint);"></div>
  <div class="abs" style="left:52px;top:113px;font-size:6.5px;line-height:10px;color:var(--white)">Phone Number<br><b>555.014.2288</b></div>
</div>

<div class="eyebrow abs" style="left:640px;top:703px;color:var(--purple)">About me</div>
<h2 class="about-title">Lena Pruvost</h2>
<div class="about-sub">Digital Business Manager</div>
<p class="about-copy">Hi! I’m so excited that you have chosen to explore my portfolio. Helping businesses achieve their goals is my passion, and I’m thrilled that with my assistance you will have more time for your own passion project. I thrive while working independently, which means you can be confident when leaving tasks for me. The type of work that lights me up is anything involving organization and/or spreadsheets. You need data analyzed that includes multiple nested if formulas? You have an overwhelming amount of email to sort through and appointments to book? I’m your gal!</p>
<div class="btn" style="left:640px;top:1016px;width:113px;height:32px"><span class="tick"><svg width="8" height="8" viewBox="0 0 10 10"><path d="M2 5l2 2 4-4" stroke="var(--teal)" stroke-width="1.6" fill="none"/></svg></span>Contact Now</div>

<!-- SERVICES -->
<svg class="abs" style="left:0;top:1195px" width="1200" height="270" viewBox="0 0 1200 270" role="img" aria-label="Faded photo of a woman working at a desk">
  <defs><linearGradient id="svcFade" x1="0" y1="0" x2="0" y2="1"><stop offset="0" stop-color="#a9cfca"/><stop offset="1" stop-color="#e9f1f0"/></linearGradient></defs>
  <path d="M0 50L600 0L1200 50V270H0Z" fill="url(#svcFade)"/>
</svg>
<div class="eyebrow abs" style="left:196px;top:1322px">Our services</div>
<h2 class="abs heading" style="left:196px;top:1342px;font-size:30px;font-weight:600">What i Do Best</h2>
<p class="abs" style="left:196px;top:1388px;width:400px;font-size:11px;line-height:17px">I thrive while working independently, which means you can be confident when leaving tasks for me.</p>

<div class="service-card faded" style="left:-14px"><svg width="30" height="30" viewBox="0 0 30 30"><rect x="6" y="3" width="18" height="24" fill="none" stroke="var(--ink)" stroke-width="1.5"/></svg><h3>Data<br>Entry</h3><span class="link">Contact Now ↗</span></div>
<div class="service-card" style="left:195px"><svg width="34" height="34" viewBox="0 0 34 34"><rect x="3" y="4" width="28" height="26" rx="2" fill="none" stroke="var(--ink)" stroke-width="1.5"/><path d="M3 10h28M8 16h10M8 21h18M8 25h14" stroke="var(--ink)" stroke-width="1.5"/></svg><h3>Content<br>Repurposing</h3><span class="link">Contact Now ↗</span></div>
<div class="service-card" style="left:404px"><svg width="40" height="34" viewBox="0 0 40 34"><circle cx="20" cy="7" r="5" fill="none" stroke="var(--ink)" stroke-width="1.5"/><circle cx="9" cy="24" r="6" fill="none" stroke="var(--ink)" stroke-width="1.5"/><circle cx="31" cy="24" r="6" fill="none" stroke="var(--ink)" stroke-width="1.5"/><path d="M20 12v10" stroke="var(--ink)" stroke-width="1.5"/></svg><h3>Financial<br>Analytics</h3><span class="link">Contact Now ↗</span></div>
<div class="service-card active" style="left:611px"><svg width="40" height="34" viewBox="0 0 40 34"><path d="M4 6h32M20 6v10M10 30l10-14 10 14" stroke="#fff" stroke-width="1.5" fill="none"/><circle cx="4" cy="6" r="3" fill="#fff"/><circle cx="36" cy="6" r="3" fill="#fff"/><circle cx="20" cy="6" r="3" fill="#fff"/></svg><h3>Graphic<br>Creations</h3><span class="link">Contact Now ↗</span></div>
<div class="service-card" style="left:818px"><svg width="40" height="36" viewBox="0 0 40 36"><circle cx="22" cy="14" r="10" fill="none" stroke="var(--ink)" stroke-width="1.5" stroke-dasharray="4 2"/><circle cx="22" cy="14" r="4" fill="none" stroke="var(--ink)" stroke-width="1.5"/><circle cx="10" cy="28" r="5" fill="none" stroke="var(--ink)" stroke-width="1.5"/></svg><h3>Project<br>Management</h3><span class="link">Contact Now ↗</span></div>
<div class="service-card faded" style="left:1027px"><svg width="36" height="34" viewBox="0 0 36 34"><rect x="3" y="6" width="28" height="24" fill="none" stroke="var(--ink)" stroke-width="1.5"/><path d="M7 24l8-8 5 5 9-10" stroke="var(--ink)" stroke-width="1.5" fill="none"/></svg><h3>Email<br>Manager</h3><span class="link">Contact Now ↗</span></div>
<div class="arrow-btn" style="left:88px;top:1539px;background:var(--white);box-shadow:0 2px 6px rgba(0,0,0,.15)"><svg width="12" height="12" viewBox="0 0 12 12"><path d="M8 1L3 6l5 5" stroke="var(--ink)" stroke-width="1.8" fill="none"/></svg></div>
<div class="arrow-btn" style="left:1065px;top:1539px;background:var(--teal)"><svg width="12" height="12" viewBox="0 0 12 12"><path d="M4 1l5 5-5 5" stroke="#fff" stroke-width="1.8" fill="none"/></svg></div>

<!-- PRICING -->
<div class="placeholder" role="img" aria-label="Cartoon avatar of Lena at a laptop" style="left:571px;top:1729px;width:59px;height:47px;background:linear-gradient(#e9d39b,#8fa3a8);border-radius:4px"></div>
<h2 class="abs heading" style="left:0;width:1200px;text-align:center;top:1796px;font-size:32px;font-weight:600">Rates And Packages</h2>
<p class="abs" style="left:350px;width:500px;text-align:center;top:1851px;font-size:11px;line-height:19px">focused on the live event and entertainment industry. Helping artists and owners to better manage their career and business by strategically reviewing systems</p>

<div class="abs" style="left:195px;top:1958px;width:815px;height:326px;background:var(--mint-pale);border-radius:10px;box-shadow:4px 4px 0 var(--ink)"></div>
<div class="abs" style="left:590px;top:1923px;width:206px;height:336px;background:var(--teal);border-radius:8px;box-shadow:4px 4px 0 var(--ink)"></div>
<div class="abs" style="left:697px;top:1939px;width:82px;height:14px;border-radius:7px;background:var(--purple);font-size:6px;color:#fff;display:flex;align-items:center;justify-content:center;letter-spacing:.5px">MOST POPULAR</div>

<div class="plan" style="left:222px;top:1986px"><div class="price">$40<small>/Hourly</small></div><div class="name">Per hour</div><div class="desc">For most businesses that want to otpimize web queries</div>
<ul><li><i></i>For clients</li><li><i></i>Needing only</li><li><i></i>Occasional help</li></ul></div>
<div class="plan" style="left:407px;top:1986px"><div class="price">$50<small>/month</small></div><div class="name">20 hours</div><div class="desc">For most businesses that want to otpimize web queries</div>
<ul><li><i></i>All limited links</li><li><i></i>Own analytics platform</li><li><i></i>Chat support</li><li><i></i>Optimize hashtags</li><li><i></i>Unlimited users</li></ul></div>
<div class="plan popular" style="left:612px;top:1958px"><div class="price">$100<small>/month</small></div><div class="name">40 hours</div><div class="desc">For most businesses that want to otpimize web queries</div>
<ul><li><i></i>All limited links</li><li><i></i>Own analytics platform</li><li><i></i>Chat support</li><li><i></i>Optimize hashtags</li><li><i></i>Unlimited users</li></ul></div>
<div class="plan" style="left:818px;top:1986px"><div class="price">$200<small>/month</small></div><div class="name">80 hours</div><div class="desc">For most businesses that want to otpimize web queries</div>
<ul><li><i></i>All limited links</li><li><i></i>Own analytics platform</li><li class="off"><i></i>Chat support</li><li><i></i>Optimize hashtags</li><li><i></i>Unlimited users</li></ul></div>

<div class="btn" style="left:222px;top:2224px;width:153px;height:32px"><span class="tick"><svg width="8" height="8" viewBox="0 0 10 10"><path d="M2 5l2 2 4-4" stroke="var(--teal)" stroke-width="1.6" fill="none"/></svg></span>Choose Plan</div>
<div class="btn" style="left:407px;top:2224px;width:153px;height:32px"><span class="tick"><svg width="8" height="8" viewBox="0 0 10 10"><path d="M2 5l2 2 4-4" stroke="var(--teal)" stroke-width="1.6" fill="none"/></svg></span>Choose Plan</div>
<div class="btn" style="left:614px;top:2199px;width:155px;height:32px;background:var(--white);color:var(--ink)"><span class="tick" style="background:var(--teal)"><svg width="8" height="8" viewBox="0 0 10 10"><path d="M2 5l2 2 4-4" stroke="#fff" stroke-width="1.6" fill="none"/></svg></span>Choose Plan</div>
<div class="btn" style="left:818px;top:2224px;width:153px;height:32px"><span class="tick"><svg width="8" height="8" viewBox="0 0 10 10"><path d="M2 5l2 2 4-4" stroke="var(--teal)" stroke-width="1.6" fill="none"/></svg></span>Choose Plan</div>

<!-- TESTIMONIALS -->
<svg class="abs" style="left:0;top:2414px" width="1200" height="535" viewBox="0 0 1200 535" role="img" aria-label="Faded photo of smiling clients">
  <defs><linearGradient id="tFade" x1="0" y1="0" x2="0" y2="1"><stop offset="0" stop-color="#a3c9c4"/><stop offset=".55" stop-color="#d5e6e3"/><stop offset="1" stop-color="#f6f7f7"/></linearGradient></defs>
  <path d="M0 45L600 0L1200 45V535H0Z" fill="url(#tFade)"/>
</svg>
<div class="eyebrow abs" style="left:0;width:1200px;text-align:center;top:2506px">Our testimonials</div>
<h2 class="abs heading" style="left:0;width:1200px;text-align:center;top:2528px;font-size:31px;font-weight:600">What Our Clients are Saying</h2>
<p class="abs" style="left:400px;width:400px;text-align:center;top:2580px;font-size:11px;line-height:18px">I thrive while working independently, which means you can be confident when leaving tasks for me.</p>
<div class="abs" style="left:195px;top:2659px;width:815px;height:266px;background:var(--mint-pale);border-radius:12px;box-shadow:4px 4px 0 var(--ink)"></div>
<svg class="abs" style="left:237px;top:2618px" width="82" height="68" viewBox="0 0 82 68"><path d="M0 68V36Q0 6 30 0l4 8Q18 14 18 30h16v38zM46 68V36Q46 6 76 0l4 8Q64 14 64 30h16v38z" fill="var(--purple)"/></svg>
<p class="quote-text">When it became apparent that a project would take more time than I had, Lena stepped up to take on the required research. She was thorough and timely; able to meet a last-minute 12-hour deadline. I would highly recommend Lena to assist with your next project.</p>
<div class="abs" style="left:0;width:1200px;text-align:center;top:2842px;font-family:Poppins,sans-serif;font-size:21px;font-weight:600;color:var(--ink)">– Dana R.</div>
<div class="abs" style="left:0;width:1200px;text-align:center;top:2880px;font-size:11.5px">Owner- Northgate Exteriors</div>
<div class="arrow-btn" style="left:170px;top:2767px;width:44px;height:44px;background:var(--teal)"><svg width="12" height="12" viewBox="0 0 12 12"><path d="M8 1L3 6l5 5" stroke="#fff" stroke-width="1.8" fill="none"/></svg></div>
<div class="arrow-btn" style="left:982px;top:2767px;width:44px;height:44px;background:var(--teal)"><svg width="12" height="12" viewBox="0 0 12 12"><path d="M4 1l5 5-5 5" stroke="#fff" stroke-width="1.8" fill="none"/></svg></div>

<!-- CONTACT -->
<div class="abs" style="left:226px;top:3042px;width:396px;height:436px;background:var(--ink);border-radius:28px"></div>
<div class="abs" style="left:230px;top:3042px;width:392px;height:430px;background:var(--teal);border-radius:28px"></div>
<h2 class="abs heading" style="left:263px;top:3082px;font-size:31px;font-weight:600;color:var(--white)">Let’s Connect</h2>
<div class="contact-item" style="top:3158px"><span class="ico"><svg width="24" height="24" viewBox="0 0 24 24"><path d="M6.6 10.8a15 15 0 006.6 6.6l2.2-2.2c.3-.3.7-.4 1-.2 1.1.4 2.3.6 3.6.6.6 0 1 .4 1 1V20c0 .6-.4 1-1 1A17 17 0 013 4c0-.6.4-1 1-1h3.5c.6 0 1 .4 1 1 0 1.3.2 2.5.6 3.6.1.3 0 .7-.2 1z" fill="none" stroke="#fff" stroke-width="1.5"/></svg></span>555.014.2288</div>
<div class="contact-item" style="top:3240px"><span class="ico"><svg width="22" height="16" viewBox="0 0 22 16"><rect x="1" y="1" width="20" height="14" rx="2" fill="none" stroke="#fff" stroke-width="1.5"/><path d="M1 2l10 7 10-7" stroke="#fff" stroke-width="1.5" fill="none"/></svg></span>LenaPruvost7@<br>mailbox.com</div>
<div class="contact-item" style="top:3322px"><span class="ico"></span>Lena M. Pruvost</div>

<div class="abs" style="left:545px;top:3084px;width:421px;height:346px;background:var(--white);border-radius:4px;box-shadow:0 4px 14px rgba(0,0,0,.1)"></div>
<h2 class="abs heading" style="left:568px;top:3114px;font-size:30px;font-weight:600">Get In Touch</h2>
<div class="field" style="left:568px;top:3173px;width:176px;height:30px">Name</div>
<div class="field" style="left:758px;top:3173px;width:178px;height:30px">Email</div>
<div class="field" style="left:568px;top:3218px;width:176px;height:30px">Phone</div>
<div class="field" style="left:758px;top:3218px;width:178px;height:30px">Address</div>
<div class="field" style="left:568px;top:3263px;width:368px;height:78px">Message</div>
<div class="btn" style="left:568px;top:3362px;width:368px;height:30px"><span class="tick"><svg width="8" height="8" viewBox="0 0 10 10"><path d="M2 5l2 2 4-4" stroke="var(--teal)" stroke-width="1.6" fill="none"/></svg></span>Connect Now</div>

<!-- FOOTER -->
<svg class="abs" style="left:0;top:3555px" width="1200" height="521" viewBox="0 0 1200 521">
  <path d="M0 40L600 0L1200 40V521H0Z" fill="var(--ink)"/>
  <path d="M0 28L600 -8L1200 28V42L600 6L0 42Z" fill="var(--teal)"/>
</svg>
<div class="placeholder" role="img" aria-label="Cartoon avatar of Lena at a laptop" style="left:538px;top:3610px;width:124px;height:103px;background:linear-gradient(#e9d39b,#8fa3a8);border-radius:6px"></div>
<h2 class="abs" style="left:196px;top:3782px;font-family:Poppins,sans-serif;font-size:25px;font-weight:600;color:var(--white)">Let’s Keep <span style="color:var(--teal)">in touch</span></h2>
<div class="abs" style="left:196px;top:3836px;width:204px;height:32px;background:var(--white);font-size:9.5px;color:var(--muted);padding:10px 12px">Enter email</div>
<div class="abs" style="left:407px;top:3836px;width:62px;height:32px;background:var(--teal);color:var(--white);font-size:10px;font-weight:600;letter-spacing:1px;display:flex;align-items:center;justify-content:center">Send</div>
<div class="abs" style="left:197px;top:3890px;display:flex;gap:14px">
  <span style="width:18px;height:18px;border-radius:50%;background:var(--white)"></span>
  <span style="width:18px;height:18px;border-radius:50%;background:var(--white)"></span>
  <span style="width:18px;height:18px;border-radius:50%;background:var(--white)"></span>
  <span style="width:18px;height:18px;border-radius:50%;background:var(--white)"></span>
</div>
<div class="abs" style="left:196px;top:3944px;font-size:10.5px;color:var(--white)">2023 © Lena Pruvost All rights reserved</div>
<div class="foot-col" style="left:671px"><h4>Get to know us</h4>Home<br>About us<br>Contact us<br>Services<br>Pricing<br>Testimonials</div>
<div class="foot-col" style="left:877px"><h4>Contact Us</h4>555.014.2288<br>LenaPruvost7@mailbox.com<br>Lena M. Pruvost</div>

</body>
</html>
```